Business card design needed

We are a Custom Joinery and specialise in design, Manufacture and Installation of kitchens and cabinetry
We currently have a logo based on the northern star in red and black but are open to something that would look fresh and clean
Updates

Project Deadline Extended
Reason: Need a couple days to go through designs. Finding some designs that are great on front and others great on reverse. I would like to be able to comment and get the total look we are after.

Target Market(s)

30-50 year olds who are looking to renovate

Industry/Entity Type

Business

Contact Information for Business Card

Larchfield Fitouts
ABN 37 418 260 573
Colin Pratley - Cabinetmaker/Designer Licence No. 318570K

Requirements
Nice to have
• Maybe a nice fresh modern kitchen picture

```html
<!DOCTYPE html>
<html lang="en">
<head>
<meta charset="utf-8">
<title>Larchfield Fitouts – Business Card</title>
<link rel="stylesheet" href="https://fonts.googleapis.com/css2?family=Righteous&display=swap">
<style>
  :root {
    --card-white: #ffffff;
    --card-edge: #9a9a9a;
    --band-charcoal: #231f20;
    --accent-red: #ff0000;
    --ink-dark: #2f3b3b;
    --text-light: #ffffff;
  }
  html, body {
    margin: 0;
    padding: 0;
    overflow: hidden;
    background: var(--card-white);
  }
  .card {
    position: relative;
    width: 1200px;
    height: 667px;
    box-sizing: border-box;
    border: 2px solid var(--card-edge);
    background: var(--card-white);
    overflow: hidden;
    font-family: "Righteous", sans-serif;
  }
  .accent-strip {
    position: absolute;
    top: 0;
    right: 0;
    width: 73px;
    height: 100%;
    background: var(--accent-red);
  }
  .brand {
    position: absolute;
    left: 120px;
    top: 160px;
    display: flex;
    align-items: center;
    gap: 22px;
  }
  .brand-mark {
    width: 46px;
    height: 46px;
    background: var(--accent-red);
  }
  .brand-name {
    margin: 0;
    font-size: 54px;
    font-weight: 400;
    letter-spacing: 2px;
    color: var(--ink-dark);
  }
  .details-band {
    position: absolute;
    left: 0;
    top: 401px;
    width: 1125px;
    height: 200px;
    background: var(--band-charcoal);
    color: var(--text-light);
    box-sizing: border-box;
    padding: 16px 0 0 68px;
  }
  .details-line {
    margin: 0;
    font-size: 38px;
    line-height: 63px;
    letter-spacing: 1px;
    white-space: nowrap;
  }
</style>
</head>
<body>
  <div class="card">
    <div class="brand">
      <div class="brand-mark"></div>
      <h1 class="brand-name">Larchfield Fitouts</h1>
    </div>
    <div class="details-band">
      <p class="details-line">Larchfield Fitouts ABN 37 418 260 573</p>
      <p class="details-line">Colin Pratley - Cabinetmaker/Designer</p>
      <p class="details-line">Licence No. 318570K</p>
    </div>
    <div class="accent-strip"></div>
  </div>
</body>
</html>
```